Corvane Thinner Logo and Packaging Design

We are seeking a striking and professional logo and packaging design for our new product line, Corvane Thinner. This logo will be used on the packaging for three different sizes of half-transparent carboys: 1L, 4L, and 20L. Corvane Thinner is a high-quality solvent brand known for its excellent solvency, fast-drying properties, and pleasant smell. The logo should feature an eagle motif to symbolize power and precision, and our slogan, "SOAR WITH PURITY." The design should be suitable for placement on hardware store and warehouse shelves. Additionally, we need the designer to create an eagle logo to accompany the packaging.

Packaging Dimensions:
1L Carboy:
Front: 71mm height x 142mm width
Side: 71mm height x 73mm width
4L Carboy:
Front: 160mm height x 170mm width
Side: 160mm height x 120mm width
20L Carboy:
Front: 245mm height x 190mm width
Side: 215mm height x 190mm width
Front Label Requirements:

Product Name: Thinner QRZ
Volume: 20L
Precautionary Statements:
Keep Away from Sources of ignition - No Smoking
Avoid Contact with Eyes
Do Not Empty into Drains or Sewers
Take Precautionary Measures Against Static Discharge
Hazard Statements:
Flammable Liquid and Vapor
May be fatal if swallowed or enters Airways
Causes Skin Irritation
Causes Serious Eye Irritation
Causes Damage to Organs if Prolonged or Repeated Exposure
Hazard Pictograms: (Include relevant hazard symbols)
Design Requirements:

Logo: Eagle motif (to be designed by the designer)
Slogan: SOAR WITH PURITY
Color Scheme: Designer to recommend (should be striking and professional for retail display)

Please see my latest picture. Kindly note the packaging is in Plastic Carboy (not in metal tin as per PS).

Eagle to be more majestic and bigger (as if soaring in the sky).
Singapore landscape as background to have Singapore identity such as TKP, Lumora Wheel, orchid near the cove etc.
Updates

Eagle to be more majestic and bigger, wings to spread wide.
We not want it to be of photo style, but more on a cartoon style. Please see my latest file uploaded.

Target Market(s)

Our target market includes painting companies, construction companies, direct household consumers, and industrial users who require high-quality solvents for various applications.

Industry/Entity Type

Chemical, spray paint and painting, household, industrial

Requirements
Must have
• Professional and Striking Design: Eye-catching and professional packaging for retail shelves. Eagle Logo: A strong, precise eagle logo. Slogan: "SOAR WITH PURITY" prominently displayed. Clear Precautionary and Hazard Statements: Important safety information and pictograms. Volume Indication: Clearly marked (e.g., 1L, 4L, 20L). Eagle to be more majestic and bigger (as if soaring in the sky). Singapore landscape as background to have Singapore identity such as TKP, Lumora Wheel, orchid near the cove etc.
Nice to have
• Color Scheme Recommendations: Suggestions for a professional, striking color scheme. Versatility: Design elements adaptable across different sizes of packaging. Environmentally Friendly Elements: Indications of sustainability or eco-friendliness in the design.
Should not have
• Overly Complex Designs: Avoid cluttered or overly intricate designs that detract from readability. Inconsistent Branding: Ensure all elements are cohesive and align with the brand identity.

```html
<!DOCTYPE html>
<html lang="en">
<head>
<meta charset="UTF-8">
<title>Corvane Thinner – Front Label</title>
<link rel="stylesheet" href="https://fonts.googleapis.com/css2?family=Montserrat:ital,wght@0,300;0,400;0,600;0,700;0,800;1,700&family=Arimo:wght@400;700&display=swap">
<style>
  :root {
    --backdrop: #767676;
    --label-white: #f4f4f4;
    --brand-red: #a8181c;
    --brand-red-light: #c42226;
    --brand-yellow: #e4bb1e;
    --ink: #222222;
    --ink-soft: #3a3a3a;
    --hazard-red: #e0161b;
    --eagle-navy: #1f3156;
    --eagle-blue: #5574a8;
    --eagle-pale: #aebfdc;
  }
  * { margin: 0; padding: 0; box-sizing: border-box; }
  html, body { width: 1200px; height: 840px; overflow: hidden; }
  body {
    background: var(--backdrop);
    position: relative;
    font-family: "Arimo", Arial, sans-serif;
  }
  .label {
    position: absolute;
    left: 242px;
    top: 69px;
    width: 715px;
    height: 702px;
    transform: scale(1.09);
    transform-origin: center center;
    background: var(--label-white);
    border-radius: 16px;
    overflow: hidden;
    box-shadow: 0 0 0 1px rgba(200, 40, 40, 0.25);
  }
  .label-bands {
    position: absolute;
    inset: 0;
    width: 715px;
    height: 702px;
  }
  .brand-block {
    position: absolute;
    left: 340px;
    width: 360px;
    text-align: center;
    color: #fff;
    font-family: "Montserrat", sans-serif;
  }
  .brand-name {
    top: 28px;
    font-weight: 800;
    font-size: 56px;
    line-height: 1;
    letter-spacing: 1px;
  }
  .brand-descriptor {
    top: 92px;
    font-weight: 400;
    font-size: 66px;
    line-height: 1;
    letter-spacing: -1px;
  }
  .slogan {
    top: 170px;
    font-weight: 700;
    font-style: italic;
    font-size: 26px;
    letter-spacing: 1.5px;
  }
  .product-name {
    top: 222px;
    font-weight: 800;
    font-size: 50px;
    line-height: 1;
    letter-spacing: 1px;
    left: 370px;
    width: 320px;
  }
  .volume {
    position: absolute;
    left: 438px;
    top: 349px;
    width: 180px;
    text-align: left;
    font-family: "Montserrat", sans-serif;
    font-weight: 600;
    font-size: 34px;
    line-height: 1;
    letter-spacing: 0.5px;
    color: var(--ink);
  }
  .safety {
    position: absolute;
    left: 41px;
    width: 380px;
  }
  .safety-precaution { top: 494px; }
  .safety-hazard { top: 582px; }
  .safety-heading {
    display: block;
    width: 215px;
    height: 18px;
    border-radius: 9px;
    background: var(--brand-red-light);
    color: #fff;
    font-weight: 700;
    font-size: 11px;
    line-height: 18px;
    text-align: center;
    letter-spacing: 0.3px;
  }
  .safety-list {
    list-style: none;
    margin-top: 10px;
    font-size: 11px;
    line-height: 12.9px;
    color: var(--ink-soft);
  }
  .safety-list li { display: flex; }
  .safety-list .num { width: 21px; }
  .pictograms {
    position: absolute;
    left: 515px;
    top: 486px;
    width: 160px;
    height: 170px;
  }
  .signal-word {
    position: absolute;
    left: 515px;
    top: 657px;
    width: 160px;
    text-align: center;
    color: var(--hazard-red);
    font-weight: 700;
    font-size: 22px;
    letter-spacing: 0.5px;
  }
</style>
</head>
<body>
  <main class="label">
    <svg class="label-bands" viewBox="0 0 715 702" xmlns="http://www.w3.org/2000/svg">
      <defs>
        <linearGradient id="eagleTones" x1="0" y1="0" x2="1" y2="1">
          <stop offset="0" stop-color="var(--eagle-pale)"/>
          <stop offset="0.45" stop-color="var(--eagle-blue)"/>
          <stop offset="1" stop-color="var(--eagle-navy)"/>
        </linearGradient>
      </defs>
      <polygon class="band-red" points="0,0 715,0 715,341 298,460 0,395" fill="var(--brand-red)"/>
      <polygon class="band-yellow" points="0,395 298,460 715,341 715,424 298,499 0,434" fill="var(--brand-yellow)"/>
      <path class="volume-tab" d="M438,341 H625 L606,391 H438 A25,25 0 0 1 438,341 Z" fill="var(--brand-yellow)"/>
      <path class="eagle-mascot" role="img" aria-label="Cartoon eagle mascot swooping down with wings spread wide, talons forward"
            d="M0,20 L40,0 L290,0 L350,120 L380,290 L350,340 L300,370 L200,485 L150,470 L110,420 L0,430 Z"
            fill="url(#eagleTones)"/>
    </svg>

    <div class="brand-block brand-name">CORVANE</div>
    <div class="brand-block brand-descriptor">THINNER</div>
    <div class="brand-block slogan">SOAR WITH PURITY</div>
    <div class="brand-block product-name">THINNER<br>QRZ</div>
    <div class="volume">4 LITERS</div>

    <section class="safety safety-precaution">
      <span class="safety-heading">PRECAUTIONARY STATEMENTS</span>
      <ol class="safety-list">
        <li><span class="num">1.</span>Keep Away from Sources of ignition - No Smoking</li>
        <li><span class="num">2.</span>Avoid Contact with Eyes</li>
        <li><span class="num">3.</span>Do Not Empty into Drains or Sewers</li>
        <li><span class="num">4.</span>Take Precautionary Measures Against Static Discharge</li>
      </ol>
    </section>

    <section class="safety safety-hazard">
      <span class="safety-heading">HAZARD STATEMENTS</span>
      <ol class="safety-list">
        <li><span class="num">1.</span>Flammable Liquid and Vapor</li>
        <li><span class="num">2.</span>May be fatal if swallowed or enters Airways</li>
        <li><span class="num">3.</span>Causes Skin Irritation</li>
        <li><span class="num">4.</span>Causes Serious Eye Irritation</li>
        <li><span class="num">5.</span>Causes Damage to Organs if Prolonged or Repeated Exposure</li>
      </ol>
    </section>

    <svg class="pictograms" viewBox="0 0 160 170" xmlns="http://www.w3.org/2000/svg" role="img" aria-label="Hazard pictograms: exclamation, health hazard, corrosive, flammable">
      <g class="pictogram pictogram-exclamation" transform="translate(38,38)">
        <rect x="-23" y="-23" width="46" height="46" transform="rotate(45)" fill="#fff" stroke="var(--hazard-red)" stroke-width="4"/>
        <rect x="-3" y="-17" width="6" height="22" rx="2" fill="#111"/>
        <circle cx="0" cy="12" r="3.5" fill="#111"/>
      </g>
      <g class="pictogram pictogram-health" transform="translate(120,38)">
        <rect x="-23" y="-23" width="46" height="46" transform="rotate(45)" fill="#fff" stroke="var(--hazard-red)" stroke-width="4"/>
        <circle cx="0" cy="-11" r="5" fill="#111"/>
        <path d="M-11,16 L-11,2 Q-11,-5 -4,-5 L4,-5 Q11,-5 11,2 L11,16 Z" fill="#111"/>
        <path d="M0,-1 L2,5 L7,5 L3,8 L5,13 L0,10 L-5,13 L-3,8 L-7,5 L-2,5 Z" fill="#fff"/>
      </g>
      <g class="pictogram pictogram-corrosive" transform="translate(38,123)">
        <rect x="-23" y="-23" width="46" height="46" transform="rotate(45)" fill="#fff" stroke="var(--hazard-red)" stroke-width="4"/>
        <path d="M-14,-12 L-4,-16 L-2,-10 L-12,-6 Z" fill="#111"/>
        <path d="M2,-14 L12,-10 L10,-5 L0,-9 Z" fill="#111"/>
        <circle cx="-8" cy="-1" r="1.5" fill="#111"/>
        <circle cx="6" cy="0" r="1.5" fill="#111"/>
        <rect x="-16" y="8" width="14" height="5" fill="#111"/>
        <rect x="2" y="8" width="14" height="5" fill="#111"/>
      </g>
      <g class="pictogram pictogram-flame" transform="translate(120,123)">
        <rect x="-23" y="-23" width="46" height="46" transform="rotate(45)" fill="#fff" stroke="var(--hazard-red)" stroke-width="4"/>
        <path d="M0,-17 C8,-8 11,-2 9,6 C7,10 3,11 0,11 C-5,11 -9,8 -9,2 C-9,-3 -5,-6 -4,-10 C-2,-6 -1,-4 0,-3 C2,-7 2,-12 0,-17 Z" fill="#111"/>
        <rect x="-11" y="13" width="22" height="4" fill="#111"/>
      </g>
    </svg>
    <div class="signal-word">WARNING</div>
  </main>
</body>
</html>
```